Upmarket cover for top management book, ideally unlike most common cover pages

This book is about both good management and mismanagement and introduces novel concepts such as the inverse exponential law in strategy, No doubt that these concepts will be criticized by some management scholars. However, students, a few other colleagues and key top managers find the new ideas useful and eye-opening.
The cover must help communicate a deeper vision of management as an expression of life creation and a sort of "divine" energy.

Practical details:
Print and ebook cover page plus elements of the cover for each of the three main book sections.
Title; The Orchard
Subtitle: Harvest methods and the spiral rising rule
Author: Teodor B. Malvezzi
Publisher: Quillstone Author Press
Width x height: 13,97 x 21,59 cm (without bleed)
Spine: 14-15 cm according to paper color

Target Market(s)

Mostly managers who did not have the opportunity of attending postgraduate management studies such as the MBA

Industry/Entity Type

Mostly high technology

Font styles to use
Serif
Sans Serif
Other font styles liked:
• Arial nova, Arial light

Requirements
Must have
• Preferably cover and back cover on white background, but any good proposals would do.
Nice to have
• An image of bright and reassuring, albeit potentially unlimited, strength. Ideally the cover design should show that good management is good for the COMMON GOOD of society
Should not have
• Please do not show images of people and no proposals reminiscent of other management and strategy book covers

```html
<!DOCTYPE html>
<html lang="en">
<head>
<meta charset="utf-8">
<title>The Orchard — Teodor B. Malvezzi</title>
<link href="https://fonts.googleapis.com/css2?family=Arimo:wght@400;700&display=swap" rel="stylesheet">
<style>
  :root {
    --page-bg: #e8e8e8;
    --cover-bg: #efefef;
    --cover-spine: #f7f7f7;
    --ink: #0a0a0a;
    --art-light: #e6e6e9;
    --art-mid: #d6d6db;
    --art-deep: #c6c6cc;
  }
  * { margin: 0; padding: 0; box-sizing: border-box; }
  html, body {
    width: 1200px;
    height: 800px;
    overflow: hidden;
    background: var(--page-bg);
  }
  .stage {
    position: relative;
    width: 1200px;
    height: 800px;
  }
  .cover {
    position: absolute;
    left: 408px;
    top: 94px;
    width: 398px;
    height: 606px;
    background: linear-gradient(90deg, var(--cover-spine) 0px, var(--cover-bg) 20px, var(--cover-bg) 100%);
    overflow: hidden;
    font-family: "Arimo", Arial, sans-serif;
    color: var(--ink);
  }
  .cover-art {
    position: absolute;
    left: 120px;
    top: 0;
    width: 278px;
    height: 606px;
    background: linear-gradient(160deg, var(--art-light) 0%, var(--art-mid) 45%, var(--art-deep) 70%, var(--art-mid) 100%);
    clip-path: polygon(55% 0%, 100% 0%, 100% 100%, 35% 100%, 30% 80%, 10% 68%, 0% 55%, 12% 38%, 30% 25%, 48% 12%);
    opacity: 0.9;
  }
  .author, .title, .subtitle { position: absolute; left: 28px; z-index: 1; }
  .author {
    top: 40px;
    font-weight: 700;
    font-size: 56px;
    line-height: 76px;
    letter-spacing: 0.03em;
    text-transform: uppercase;
    white-space: nowrap;
  }
  .title {
    top: 310px;
    font-weight: 400;
    font-size: 68px;
    line-height: 81px;
    text-transform: uppercase;
    white-space: nowrap;
  }
  .subtitle {
    top: 509px;
    width: 300px;
    font-weight: 400;
    font-size: 18px;
    line-height: 22px;
  }
</style>
</head>
<body>
  <main class="stage">
    <section class="cover">
      <div class="cover-art" role="img" aria-label="Low-poly wireframe figure of connected points and lines in soft greys"></div>
      <h2 class="author">Teodor B.<br>Malvezzi</h2>
      <h1 class="title">The<br>Orchard</h1>
      <p class="subtitle">Harvest methods and the spiral rising rule</p>
    </section>
  </main>
</body>
</html>
```